Business Card and Banner Design

We have a logo design that we choose out of a contest already. The logo design was great but nfortunately, the person who designs the logo hasn't been able to come up with a business card that we like.

So here it is, we have a logo already. We want a business card layout options. We also want banner design as well. Two banner design that is going around our projects. I will attach a few pictures of other designs.

We are also looking for suggestion on the logo font. We would like a better font that makes the logo and slogan stand out a little more.

Deliverable 1 New Business Card
Deliverable 2 - New Fence Banner/Poster

```html
<!DOCTYPE html>
<html lang="en">
<head>
<meta charset="utf-8">
<title>Norvale Group – Business Card</title>
<link rel="stylesheet" href="https://fonts.googleapis.com/css2?family=Montserrat:wght@500;700;800&family=Tinos:wght@400;700&display=swap">
<style>
  :root{
    --stage:#6f6a64;
    --card-deep:#2a3fa6;
    --card-mid:#2f4cb8;
    --card-light:#4a89d4;
    --white:#ffffff;
    --shadow:rgba(0,0,0,.35);
  }
  *{margin:0;padding:0;box-sizing:border-box;}
  html,body{width:1200px;height:1200px;overflow:hidden;}
  body{background:var(--stage);position:relative;font-family:"Montserrat",Arial,sans-serif;color:var(--white);}

  .card{position:absolute;width:560px;height:336px;overflow:hidden;box-shadow:0 6px 18px var(--shadow);}
  .card-back{left:517px;top:235px;background:var(--card-deep);}
  .card-front{left:152px;top:618px;background:var(--card-deep);}
  .card-bg{position:absolute;inset:0;width:100%;height:100%;}

  .brand{position:absolute;display:flex;flex-direction:column;align-items:center;font-family:"Montserrat",Arial,sans-serif;font-weight:800;color:var(--white);letter-spacing:.5px;white-space:nowrap;line-height:1;}
  .brand-dot{display:block;border:5px solid var(--white);border-radius:50%;}
  .card-back .brand{left:0;right:0;top:90px;font-size:32px;gap:26px;}
  .card-back .brand-dot{width:60px;height:60px;}
  .card-front .brand{left:288px;width:240px;top:46px;font-size:20px;gap:14px;}
  .card-front .brand-dot{width:38px;height:38px;border-width:4px;}

  .person-name{position:absolute;left:31px;top:146px;font-size:27px;font-weight:700;letter-spacing:1px;}
  .person-role{position:absolute;left:33px;top:188px;font-size:15px;font-weight:500;font-family:Arial,"Montserrat",sans-serif;}

  .contact-list{position:absolute;left:31px;top:222px;list-style:none;font-family:"Tinos","Times New Roman",serif;font-size:21px;line-height:31px;}
  .contact-list li{display:flex;align-items:center;gap:8px;}
  .contact-list svg{width:18px;height:18px;flex:none;}

  .divider{position:absolute;left:318px;top:184px;width:4px;height:122px;background:var(--white);}

  .location{position:absolute;left:330px;top:212px;font-family:"Tinos","Times New Roman",serif;font-style:normal;}
  .location-area{font-size:23px;font-weight:700;letter-spacing:.5px;}
  .location-city{font-size:21px;}
  .location-pin{position:absolute;left:402px;top:272px;width:24px;height:30px;}
</style>
</head>
<body>

  <section class="card card-back" aria-label="Business card back">
    <div class="brand"><span class="brand-dot"></span>NORVALE GROUP</div>
  </section>

  <section class="card card-front" aria-label="Business card front">
    <svg class="card-bg" viewBox="0 0 560 336" preserveAspectRatio="none" aria-hidden="true">
      <rect width="560" height="336" fill="var(--card-deep)"/>
      <polygon points="0,0 560,0 560,150 430,196 0,70" fill="var(--card-mid)"/>
      <polygon points="150,0 560,0 560,118 440,170 120,0" fill="var(--card-light)"/>
    </svg>

    <div class="brand"><span class="brand-dot"></span>NORVALE GROUP</div>

    <h1 class="person-name">DAREN HOLT</h1>
    <p class="person-role">Chairman and CEO</p>

    <ul class="contact-list">
      <li>
        <svg viewBox="0 0 20 20" aria-hidden="true"><circle cx="10" cy="10" r="8.5" fill="none" stroke="#fff" stroke-width="1.6"/><path d="M7 5.5l1.6 2.4-1 1.2a6 6 0 0 0 3.3 3.3l1.2-1 2.4 1.6-.8 1.6c-3.8.2-8-4-7.8-7.8z" fill="#fff"/></svg>
        16045550142
      </li>
      <li>
        <svg viewBox="0 0 20 20" aria-hidden="true"><rect x="2" y="4.5" width="16" height="11" fill="none" stroke="#fff" stroke-width="1.6"/><path d="M2 5l8 6 8-6" fill="none" stroke="#fff" stroke-width="1.6"/></svg>
        holt@norvalegroup.com
      </li>
      <li>
        <svg viewBox="0 0 20 20" aria-hidden="true"><circle cx="10" cy="10" r="8" fill="none" stroke="#fff" stroke-width="1.6"/><ellipse cx="10" cy="10" rx="3.5" ry="8" fill="none" stroke="#fff" stroke-width="1.4"/><path d="M2 10h16" stroke="#fff" stroke-width="1.4"/></svg>
        www.norvalegroup.com
      </li>
    </ul>

    <span class="divider"></span>

    <address class="location">
      <div class="location-area">Upper Ridge</div>
      <div class="location-city">Eastvale, Canada</div>
    </address>
    <svg class="location-pin" viewBox="0 0 24 30" aria-hidden="true"><path d="M12 1a10 10 0 0 0-10 10c0 7 10 18 10 18s10-11 10-18A10 10 0 0 0 12 1z" fill="#fff"/><circle cx="12" cy="11" r="3.6" fill="var(--card-deep)"/></svg>
  </section>

</body>
</html>
```